I'm looking for strong image and design for the first book in a series titled "Bernard Whitcombe On A Voyage Through Our Convictions" subtitle "Finding a Footing in Living"; although it's about beliefs, I'm not look for an ethereal feel as the first book is about how our beliefs impact our actions and expectations. I'm a published philosopher and keen on branding my name for professional purposes hence the use of my name :) The book will initially be an e-book but I will follow up with a paperback soon afterwards. My website http://bernardwhitcombe-example.com/ may provide some help on me and my projects. Thanks, Bern

Target Market(s)

Graduates and corporate folk who tend to lose their way in the systems.

Logo Text

Bernard Whitcombe on Convictions

Font styles to use
Sans Serif

Colors

Designer to choose colors to be used in the design.

Requirements
Must have
• Needless to say, but impact.
Nice to have
• Strong colours
Should not have
• Religious imagery; the book is philosophical and leans into living in this world.

```html
<!DOCTYPE html>
<html lang="en">
<head>
<meta charset="utf-8">
<title>Bernard Whitcombe – On A Voyage Through Our Convictions</title>
<link rel="stylesheet" href="https://fonts.googleapis.com/css2?family=Nunito+Sans:wght@400;500&family=Barlow:wght@500&display=swap">
<style>
  :root {
    --cover-bg: #e1eef4;
    --ink-navy: #062842;
    --author-violet: #4b4c9c;
    --arrow-orange: #f2a93b;
    --arrow-red: #e2473a;
    --arrow-sky: #a9d8de;
  }
  html, body {
    margin: 0;
    padding: 0;
    overflow: hidden;
  }
  body {
    width: 802px;
    height: 1200px;
    background: var(--cover-bg);
  }
  .book-cover {
    position: relative;
    width: 802px;
    height: 1200px;
    background: var(--cover-bg);
    overflow: hidden;
  }
  .author-name {
    position: absolute;
    top: 52px;
    left: 0;
    width: 100%;
    margin: 0;
    text-align: center;
    font-family: "Nunito Sans", sans-serif;
    font-weight: 500;
    font-size: 32px;
    letter-spacing: 0.2em;
    color: var(--author-violet);
  }
  .book-title {
    position: absolute;
    top: 146px;
    left: 0;
    width: 100%;
    margin: 0;
    text-align: center;
    font-family: "Nunito Sans", sans-serif;
    font-weight: 400;
    font-size: 68px;
    line-height: 90px;
    color: var(--ink-navy);
  }
  .book-title span {
    display: block;
  }
  .cover-illustration {
    position: absolute;
    left: 182px;
    top: 432px;
    width: 438px;
    height: 580px;
    background: linear-gradient(180deg,
      var(--arrow-sky) 0%,
      var(--arrow-orange) 20%,
      var(--arrow-red) 36%,
      var(--ink-navy) 52%,
      var(--ink-navy) 100%);
    border-radius: 6px;
  }
  .book-subtitle {
    position: absolute;
    top: 1082px;
    left: 0;
    width: 100%;
    margin: 0;
    text-align: center;
    font-family: "Barlow", sans-serif;
    font-weight: 500;
    font-size: 33px;
    letter-spacing: 0.16em;
    color: var(--ink-navy);
  }
</style>
</head>
<body>
  <main class="book-cover">
    <p class="author-name">BERNARD WHITCOMBE</p>
    <h1 class="book-title">
      <span>On A Voyage Through</span>
      <span>Our Convictions</span>
    </h1>
    <div class="cover-illustration" role="img" aria-label="Illustration of a dark navy head in profile with many colourful arrows bursting out of the top in all directions"></div>
    <p class="book-subtitle">FINDING A FOOTING IN LIVING</p>
  </main>
</body>
</html>
```